Real Estate Investment Education Sales company needs Advertisement Design

We have agreed to place a cover ad in a booklet that will sit on local restaurant tables. The idea behind the booklets are that while people are waiting for their meal to arrive, they will look at the booklet on the table and begin reading it. Teh booklet will contain ads and trivia questions.
The Ad dimensions are 3.75 inches wide by 5.98 Inches high.
I have several examples of ads that have been done in the past, but I am not sure if the source materials are in a high enough resolution.
The purpose of the ad is to pique the diners interest so they scan the QR Code (provided at a later date), call or visit the website to get more information on how they can become a real estate investor. The actual company that provides the real estate investing training is called Velquor. www.learn.myvelquor-demo.com.
The Ad will be accompanied by a 300 word article about the advantages of becoming a real estate investor. This will be written separately to go along with the ad, but it is not a part of this gig. The article will appear next to the ad, and will not be a part of the graphic.
As mentioned, I will provide ad samples and may be able to get high-res images of certain components of the ads, if necessary.
The ad that I like the best (see attached) is the one with the ladies, the check and the pics of the house, but I am certainly open to other ideas. I am including files with samples and my company logo. I need to have the phone number 555-184-7260 and logo included in the ad, but not as a major part.
Target Market(s)
Adults looking to better their financial position by purchasing RE Investment Education
Industry/Entity Type
Real Estate
Font styles to use
Requirements
Must have
- Space in ad for QR code to be placed at a later date. Company logo and phone number of 555-184-7260
Nice to have
- see attached ad samples
Should not have
- Velquor Logo or Mention of Velquor

```html
<!DOCTYPE html>
<html lang="en">
<head>
<meta charset="utf-8">
<title>Real Estate Investing Ad</title>
<link href="https://fonts.googleapis.com/css2?family=Roboto+Condensed:wght@300;400;700&display=swap" rel="stylesheet">
<style>
  :root {
    --red: #c4161c;
    --black: #231f20;
    --white: #ffffff;
    --ink: #1c1c1c;
    --backdrop: #eeeeee;
  }
  * { margin: 0; padding: 0; box-sizing: border-box; }
  html, body { width: 1200px; height: 960px; overflow: hidden; background: var(--backdrop); }
  body { font-family: "Roboto Condensed", "Arial Narrow", sans-serif; }

  .ad {
    position: absolute; left: 295.5px; top: -5px;
    width: 609px; height: 970px;
    transform: scale(0.94); transform-origin: center center;
    background: var(--white); overflow: hidden;
    box-shadow: 0 10px 30px rgba(0,0,0,.12);
  }

  .hero-band { position: absolute; left: 0; top: 0; width: 609px; height: 342px; background: var(--red); overflow: hidden; }
  .check-photo {
    position: absolute; left: -60px; top: 95px; width: 420px; height: 205px;
    transform: rotate(-22deg);
    background: linear-gradient(135deg, #e3eeec 0%, #c9dcd8 100%);
    box-shadow: 0 4px 10px rgba(0,0,0,.25);
  }
  .team-photo {
    position: absolute; left: 290px; top: 60px; width: 290px; height: 250px;
    transform: rotate(14deg); z-index: 3;
    background: var(--white); padding: 8px;
    box-shadow: 0 5px 14px rgba(0,0,0,.35);
  }
  .team-photo .fill { width: 100%; height: 100%; background: linear-gradient(160deg, #6d6a63 0%, #b9b4aa 55%, #e6e2da 100%); }

  .progress-strip { position: absolute; left: 0; top: 342px; width: 609px; height: 161px; }
  .stage-photo { position: absolute; top: 0; height: 161px; }
  .stage-before { left: 0; width: 240px; background: linear-gradient(180deg, #dfe3e8 0%, #b7bcc2 55%, #e8e8e6 100%); }
  .stage-gutted { left: 190px; width: 230px; background: linear-gradient(180deg, #8a6b52 0%, #b79878 55%, #d8c6b0 100%); }
  .stage-after { left: 410px; width: 199px; background: linear-gradient(180deg, #e6eaee 0%, #bfc3c6 50%, #d9d6cc 100%); }
  .chevrons { position: absolute; left: 0; top: 0; }
  .stage-label {
    position: absolute; bottom: -9px; color: var(--white);
    font-weight: 700; font-size: 46px; line-height: 1;
    text-shadow: 0 1px 3px rgba(0,0,0,.35);
  }

  .pitch { position: absolute; left: 0; top: 503px; width: 609px; text-align: center; color: var(--ink); }
  .pitch-lead { margin-top: 28px; font-size: 49px; font-weight: 400; line-height: 1; letter-spacing: -0.5px; }
  .pitch-headline { margin-top: 3px; font-size: 50px; font-weight: 700; color: var(--red); line-height: 1; letter-spacing: -0.8px; }
  .pitch-sub { margin-top: 6px; font-size: 27px; font-weight: 700; line-height: 1; }
  .pitch-benefits { margin-top: 28px; font-size: 26px; font-weight: 300; color: var(--red); line-height: 1; }
  .pitch-support { margin-top: 12px; font-size: 19px; font-weight: 700; line-height: 1; }

  .footer { position: absolute; left: 0; top: 781px; width: 609px; height: 189px; }
  .footer svg { position: absolute; left: 0; top: 0; }
  .qr-slot { position: absolute; left: 34px; top: 29px; width: 121px; height: 122px; background: var(--white); }
  .learn-more { position: absolute; left: 182px; top: 36px; color: var(--white); }
  .learn-more svg { position: static; display: block; margin-bottom: 8px; }
  .learn-more-text { font-size: 37px; font-weight: 700; line-height: 0.98; }
  .brand-name { position: absolute; right: 32px; top: 66px; color: var(--white); font-size: 26px; font-weight: 700; line-height: 1; }
  .phone { position: absolute; right: 31px; top: 124px; color: var(--white); font-size: 25px; font-weight: 700; line-height: 1; }
</style>
</head>
<body>
<main class="ad">
  <section class="hero-band">
    <div class="check-photo" role="img" aria-label="Photo of a large commission check"></div>
  </section>
  <div class="team-photo"><div class="fill" role="img" aria-label="Photo of three women investors standing by a piano"></div></div>

  <section class="progress-strip">
    <div class="stage-photo stage-before" role="img" aria-label="Photo of the house before renovation"></div>
    <div class="stage-photo stage-gutted" role="img" aria-label="Photo of the house interior gutted to the studs"></div>
    <div class="stage-photo stage-after" role="img" aria-label="Photo of the renovated house"></div>
    <svg class="chevrons" width="609" height="161" viewBox="0 0 609 161">
      <polygon points="183,0 190,0 243,80 197,161 190,161 236,80" fill="var(--red)"/>
      <polygon points="396,0 403,0 430,80 384,161 377,161 423,80" fill="var(--red)"/>
    </svg>
    <span class="stage-label" style="left:38px">Before</span>
    <span class="stage-label" style="left:230px">Gutted</span>
    <span class="stage-label" style="left:468px">After</span>
  </section>

  <section class="pitch">
    <p class="pitch-lead">Learn How These 3 Ladies</p>
    <h1 class="pitch-headline">BUILT A 6 FIGURE INCOME</h1>
    <p class="pitch-sub">IN REAL ESTATE IN ONLY A FEW MONTHS!</p>
    <p class="pitch-benefits">None Of Their Money • None Of Their Credit</p>
    <p class="pitch-support">Local Group • Ongoing Training &amp; Support</p>
  </section>

  <footer class="footer">
    <svg width="609" height="189" viewBox="0 0 609 189">
      <polygon points="0,0 418,0 443,40 293,189 0,189" fill="var(--red)"/>
      <polygon points="333,40 609,40 609,189 293,189" fill="var(--black)"/>
    </svg>
    <div class="qr-slot" aria-label="Space for QR code"></div>
    <div class="learn-more">
      <svg width="38" height="38" viewBox="0 0 38 38">
        <circle cx="19" cy="19" r="16" fill="none" stroke="var(--white)" stroke-width="3.5"/>
        <path d="M27 19H12M18 12l-7 7 7 7" fill="none" stroke="var(--white)" stroke-width="3.5"/>
      </svg>
      <div class="learn-more-text">LEARN<br>MORE</div>
    </div>
    <div class="brand-name">Brickline</div>
    <div class="phone">Phone: 555-184-7260</div>
  </footer>
</main>
</body>
</html>
```